Create a pouch design for a new sports supplement product

Dimensions are 235mm (width) x 335mm (length) x 110mm (gusset)
File 1 - Extension of design brief please read both briefs
File 2 - Is 2 potential pouches this is just to give you a better example of size the dimensions are for the pouch on the right. This picture is not to give you design ideas as I am not very keen on either of these designs.
We need a design to be printed onto the pouches of our whey protein product. The brand name is 'Stellar Fuelworks' and needs to be displayed on the packaging either just writing or a simple logo design. I am not the most creative person in the world but have put together a more detailed brief listing some of the key information that needs to be included on the pouch (See attachment) Please feel free if you have experience of this the sports supplement market or have different ideas then please feel free to explore them.
The pouch would either be printed straight onto the pouch, or possibly just a printed label (front & back) to be stuck onto the pouch. Please design either or both.
Open to different colour schemes. Design has to be modern looking and eye-catching.
Some key points;
High quality whey protein concentrate
All Natural
Soy free
Great tasting
Please google image search 'protein pouches' to see other designs if your not familiar with the sports supplement market.
Any questions feel free to ask.
Updates
Hi, Thanks for all your design! I am really busy at the moment so haven't had chance to give feedback and have a proper look through all the designs. I have extended the time frame to give myself chance to give proper feedback and see any changes needed. Expect feedback sunday at the latest, and I will be pick a design early next week.
Target Market(s)
Sports supplement market. Product is a whey protein shake
Industry/Entity Type
Nutrition
Look and feel
Each slider illustrates characteristics of the customer's brand and the style your logo design should communicate.

```html
<!DOCTYPE html>
<html lang="en">
<head>
<meta charset="utf-8">
<title>Stellar Fuelworks – Natural Whey Protein Pouch</title>
<link href="https://fonts.googleapis.com/css2?family=Orbitron:wght@800&family=Roboto+Condensed:wght@400&family=Arimo:wght@700&family=Michroma&family=Alfa+Slab+One&display=swap" rel="stylesheet">
<style>
  :root {
    --bg-top: #2b2d33;
    --bg-mid: #1c1e23;
    --bg-bottom: #0d0e11;
    --brand-red: #a8092a;
    --white: #ffffff;
    --dash-red: #b10a2d;
  }
  * { margin: 0; padding: 0; box-sizing: border-box; }
  html, body { width: 842px; height: 1200px; overflow: hidden; background: var(--bg-bottom); }
  .pouch {
    position: relative;
    width: 842px; height: 1200px; overflow: hidden;
    background:
      repeating-linear-gradient(135deg, rgba(255,255,255,0.025) 0 2px, transparent 2px 6px),
      linear-gradient(180deg, var(--bg-top) 0%, var(--bg-mid) 45%, var(--bg-bottom) 100%);
    color: var(--white);
  }
  .cut-line { position: absolute; left: 0; top: 22px; width: 842px; height: 40px; }
  .reseal-band {
    position: absolute; left: 0; top: 92px; width: 842px; height: 44px;
    background: var(--brand-red);
  }
  .reseal-band span {
    position: absolute; right: 79px; top: 12px;
    font-family: "Michroma", sans-serif; font-size: 15px; letter-spacing: 0.5px;
  }
  .brand-vertical {
    position: absolute; left: 88px; top: 788px;
    transform: rotate(-90deg); transform-origin: left top;
    font-family: "Roboto Condensed", sans-serif; font-size: 40px; line-height: 1;
    white-space: nowrap; letter-spacing: 0.5px;
  }
  .product-title {
    position: absolute; left: 145px; top: 528px;
    font-family: "Orbitron", sans-serif; font-weight: 800;
    font-size: 76px; line-height: 95px; letter-spacing: 2px;
  }
  .natural-stamp {
    position: absolute; left: 574px; top: 428px; width: 188px; height: 98px;
    border: 3px solid var(--white); border-radius: 10px;
    transform: rotate(9deg);
    font-family: "Alfa Slab One", serif; text-align: center; line-height: 1;
    padding-top: 12px;
  }
  .natural-stamp .pct { display: block; font-size: 38px; }
  .natural-stamp .word { display: block; font-size: 27px; margin-top: 3px; }
  .divider { position: absolute; left: 77px; top: 806px; width: 765px; height: 6px; background: var(--brand-red); }
  .flavour {
    position: absolute; left: 80px; top: 822px;
    font-family: "Michroma", sans-serif; font-size: 16px; letter-spacing: 3px;
  }
  .benefits {
    position: absolute; left: 80px; top: 848px; list-style: none;
    font-family: "Arimo", sans-serif; font-weight: 700; font-size: 15px; line-height: 20px;
  }
  .net-weight {
    position: absolute; right: 93px; top: 818px; text-align: center;
    font-family: "Arimo", sans-serif; font-weight: 700;
  }
  .net-weight .grams { display: block; font-size: 29px; line-height: 34px; }
  .net-weight .servings { display: block; font-size: 18px; line-height: 20px; }
  .feature-icons { position: absolute; left: 264px; top: 1020px; display: flex; gap: 14px; }
  .feature { width: 96px; text-align: center; }
  .feature svg { width: 96px; height: 96px; display: block; }
  .feature-label {
    display: block; margin-top: 6px; color: var(--brand-red);
    font-family: "Michroma", sans-serif; font-size: 13px; letter-spacing: 1px;
  }
</style>
</head>
<body>
<main class="pouch">
  <svg class="cut-line" viewBox="0 0 842 40" aria-hidden="true">
    <line x1="0" y1="20" x2="842" y2="20" stroke="var(--dash-red)" stroke-width="3" stroke-dasharray="14 8"/>
    <g fill="none" stroke="var(--dash-red)" stroke-width="3">
      <circle cx="747" cy="10" r="6"/>
      <circle cx="747" cy="30" r="6"/>
      <line x1="752" y1="14" x2="720" y2="27"/>
      <line x1="752" y1="26" x2="720" y2="13"/>
    </g>
  </svg>

  <div class="reseal-band"><span>RESEAL HERE FOR FRESHNESS</span></div>

  <div class="brand-vertical">STELLAR FUELWORKS</div>

  <div class="natural-stamp"><span class="pct">100%</span><span class="word">NATURAL</span></div>

  <h1 class="product-title">NATURAL<br>WHEY<br>PROTEIN</h1>

  <div class="divider"></div>

  <p class="flavour">STRAWBERRY FLAVOUR</p>
  <ul class="benefits">
    <li>No artificial Flavours</li>
    <li>Excellent Amino acid profile</li>
    <li>80% high quality protein content</li>
    <li>Soy free</li>
  </ul>

  <div class="net-weight"><span class="grams">909g</span><span class="servings">30 servings</span></div>

  <div class="feature-icons">
    <div class="feature">
      <svg viewBox="0 0 96 96" aria-hidden="true">
        <circle cx="48" cy="48" r="47" fill="var(--brand-red)"/>
        <g fill="var(--white)">
          <rect x="20" y="36" width="8" height="24" rx="2"/>
          <rect x="29" y="31" width="9" height="34" rx="2"/>
          <rect x="38" y="45" width="20" height="6"/>
          <rect x="58" y="31" width="9" height="34" rx="2"/>
          <rect x="68" y="36" width="8" height="24" rx="2"/>
        </g>
      </svg>
      <span class="feature-label">BUILD</span>
    </div>
    <div class="feature">
      <svg viewBox="0 0 96 96" aria-hidden="true">
        <circle cx="48" cy="48" r="47" fill="var(--brand-red)"/>
        <g stroke="var(--white)" stroke-width="3">
          <line x1="34" y1="30" x2="46" y2="42"/>
          <line x1="46" y1="42" x2="62" y2="34"/>
          <line x1="46" y1="42" x2="50" y2="58"/>
          <line x1="50" y1="58" x2="38" y2="70"/>
        </g>
        <g fill="var(--white)">
          <circle cx="34" cy="30" r="5"/>
          <circle cx="46" cy="42" r="6"/>
          <circle cx="62" cy="34" r="5"/>
          <circle cx="50" cy="58" r="6"/>
          <circle cx="38" cy="70" r="5"/>
        </g>
      </svg>
      <span class="feature-label">GROW</span>
    </div>
    <div class="feature">
      <svg viewBox="0 0 96 96" aria-hidden="true">
        <circle cx="48" cy="48" r="47" fill="var(--brand-red)"/>
        <path d="M50 22 C66 34 66 56 50 70 C36 58 36 36 50 22 Z" fill="var(--white)"/>
        <path d="M50 30 L50 66 M50 70 L42 78" stroke="var(--brand-red)" stroke-width="2.5" fill="none"/>
        <path d="M50 70 L42 78" stroke="var(--white)" stroke-width="3" fill="none"/>
      </svg>
      <span class="feature-label">NATURAL</span>
    </div>
  </div>
</main>
</body>
</html>
```